New business card design for Pinecrest Hollow Optometry Clinic

We need a new business card design using our existing logo (uploaded). Please do not include eyes, eye exam charts or beaches, water, sand. The logo I uploaded shows our colors of green and blue, but we are open to seeing it in black OR white. We would like to see something modern and fresh. It will need to be 2 sided. On the front we will need to be able to put a doctors name, for example-Dr Marta Kellerman and Associates. We will need to be able to change the name to other doctors names when we send for printing. The back of the card should list the following: 3817 Tarrow St, Wasaga Beach (P)705-555-0148 (E) info@phoc.ca www.phoc.ca. "We are welcoming new patients" and a line for the appointment date and time. I have uploaded the back of a card to give an example

```html
<!DOCTYPE html>
<html lang="en">
<head>
<meta charset="utf-8">
<title>Pinecrest Hollow Optometry Clinic – Business Card</title>
<link href="https://fonts.googleapis.com/css2?family=Lato:wght@400;700;900&family=Crimson+Pro:wght@500;600&display=swap" rel="stylesheet">
<style>
  :root {
    --backdrop: #2b2d31;
    --card-dark: #1c1c1e;
    --mark-dark: #4a4a4d;
    --card-light: #ffffff;
    --brand-blue: #2b3f9a;
    --brand-green: #1f9a45;
    --rule-grey: #5c5c5c;
    --text-grey: #55585c;
  }
  * { box-sizing: border-box; margin: 0; padding: 0; }
  html, body { width: 1200px; height: 952px; overflow: hidden; }
  body {
    background: var(--backdrop);
    font-family: "Lato", Arial, sans-serif;
    position: relative;
  }
  .card {
    position: absolute;
    width: 490px;
    height: 280px;
    border-radius: 3px;
    box-shadow: 0 10px 30px rgba(0,0,0,.45);
  }
  /* Front */
  .card--front {
    left: 80px; top: 336px;
    background: var(--card-dark);
    display: flex; align-items: center; justify-content: center;
  }
  .front-brand {
    display: flex; align-items: center; gap: 14px;
    color: var(--mark-dark);
    font-weight: 700;
    font-size: 22px;
    line-height: 1.2;
  }
  .brand-dot {
    width: 22px; height: 22px; border-radius: 50%;
    background: var(--mark-dark); flex: none;
  }
  /* Back */
  .card--back {
    left: 630px; top: 336px;
    background: var(--card-light);
    padding: 26px 30px 0 30px;
  }
  .back-brand {
    display: flex; align-items: center; justify-content: center; gap: 8px;
    color: var(--brand-blue);
    font-weight: 700;
    font-size: 15px;
  }
  .back-brand .brand-dot { width: 12px; height: 12px; background: var(--brand-green); }
  .headline {
    margin-top: 14px;
    color: var(--brand-green);
    font-weight: 900;
    font-size: 23px;
    letter-spacing: .2px;
    text-transform: uppercase;
    text-align: center;
  }
  .field-row { display: flex; align-items: flex-end; gap: 8px; margin-top: 16px; }
  .field-label {
    font-family: "Crimson Pro", Georgia, serif;
    font-weight: 600;
    font-size: 15px;
    white-space: nowrap;
  }
  .field-label--blue { color: var(--brand-blue); }
  .field-label--green { color: var(--brand-green); }
  .field-line { flex: 1; border-bottom: 1.5px solid var(--rule-grey); height: 1px; margin-bottom: 4px; }
  .contact-row {
    display: flex; justify-content: space-between; align-items: center;
    margin-top: 22px;
    color: var(--text-grey);
    font-size: 13px;
  }
  .contact-item { display: flex; align-items: center; gap: 6px; }
  .contact-icon {
    width: 16px; height: 16px; border-radius: 2px;
    background: var(--brand-blue);
    display: flex; align-items: center; justify-content: center;
  }
  .address {
    margin-top: 8px;
    text-align: center;
    color: var(--text-grey);
    font-size: 13px;
    letter-spacing: .4px;
  }
</style>
</head>
<body>
  <section class="card card--front" aria-label="Card front">
    <div class="front-brand">
      <span class="brand-dot"></span>
      <span class="brand-name">Pinecrest Hollow<br>Optometry Clinic</span>
    </div>
  </section>

  <section class="card card--back" aria-label="Card back">
    <div class="back-brand">
      <span class="brand-dot"></span>
      <span class="brand-name">Pinecrest Hollow Optometry Clinic</span>
    </div>
    <h1 class="headline">We are welcoming new patients</h1>

    <div class="field-row">
      <span class="field-label field-label--blue">Doctors Name</span>
      <span class="field-line"></span>
    </div>
    <div class="field-row">
      <span class="field-label field-label--green">Date</span>
      <span class="field-line"></span>
      <span class="field-label field-label--green">Time</span>
      <span class="field-line"></span>
    </div>

    <div class="contact-row">
      <span class="contact-item">
        <span class="contact-icon">
          <svg width="10" height="10" viewBox="0 0 24 24"><path fill="#fff" d="M6.6 10.8a15.1 15.1 0 0 0 6.6 6.6l2.2-2.2c.3-.3.7-.4 1-.2 1.1.4 2.3.6 3.6.6.6 0 1 .4 1 1V20c0 .6-.4 1-1 1A17 17 0 0 1 3 4c0-.6.4-1 1-1h3.5c.6 0 1 .4 1 1 0 1.3.2 2.5.6 3.6.1.3 0 .7-.2 1z"/></svg>
        </span>
        705-555-0148
      </span>
      <span class="contact-item">
        <span class="contact-icon">
          <svg width="10" height="10" viewBox="0 0 24 24"><path fill="none" stroke="#fff" stroke-width="2.5" d="M3 6h18v12H3z M3 6l9 7 9-7"/></svg>
        </span>
        info@phoc.ca
      </span>
      <span class="contact-item">
        <span class="contact-icon">
          <svg width="10" height="10" viewBox="0 0 24 24"><path fill="#fff" d="M5 3l14 9-6 1.5 3.5 6.5-2.6 1.4-3.5-6.6L5 19z"/></svg>
        </span>
        www.phoc.ca
      </span>
    </div>
    <p class="address">3817 Tarrow St, Wasaga Beach</p>
  </section>
</body>
</html>
```